Business Card Design

Copperfield Lantern & Spark, Inc. (CLS), located in Memphis, TN began operating on 2003. We are a certified
minority woman-owned business that genuinely takes a vested interest in our customers. We serve utilities,
government, contractors and end user markets in electrical, water, gas and industrial supplies. Our core
competency as a distributor of electrical materials has positioned us to serve business of all size. As your supply
chain partner, we arm you with the resources you need to make your supply chain more efficient. Our team
works with your team on a daily basis to help you solve problems and achieve goals. This team approach has
helped CLS customers to succeed and we can do the same for you.

NAICS Codes:
423610 Electrical Apparatus and Equipment, Wiring Supplies, and Related Equipment Merchant
Wholesalers
423510 Metal Service Centers and Other Metal Merchant Wholesalers
423720 Plumbing and Heating Equipment and Supplies (Hydronics) Merchant Wholesalers

Certifications
MBE (KRVPQAL, State of Tennessee Up-MRX and FJW), WBE (HQOLT),
WOSB, DOT (TDOT, MDOT, ALDOT, SCDOT, NCDOT, and VDOT), LOSB,
SBE, and LSB Certified
Some of Our Products Include:
. Boxes & Covers
. Conduit & Raceway
. Fittings
. Fuses
. Lamp & Ballasts
. Lighting Controls & Timers
. Lighting Fixtures
. Personal Safety
. Pipes
. Power Distribution
. Terminations Ground & Splices
. Tools & Testers
. Wire, Cords & Cable
. Wiring Devices
. Valves

Industry/Entity Type

Business

Contact Information for Business Card

Marianne T. Holloway - President/CEO
4728 Quillon Ave., Memphis, TN 38127
901-555-0147 office, 901-555-0182 fax, 901-555-0163 cell
mtholloway@clsllc-example.com - www.clsincorp-example.com

```html
<!DOCTYPE html>
<html lang="en">
<head>
<meta charset="utf-8">
<title>Copperfield Lantern &amp; Spark, Inc. — Business Card</title>
<link rel="stylesheet" href="https://fonts.googleapis.com/css2?family=Cardo:ital,wght@0,400;0,700;1,400&display=swap">
<style>
  :root {
    --backdrop: #d6d6d6;
    --paper: #f7f7f5;
    --ink: #111111;
    --olive: #7a7f3e;
    --olive-text: #8c8f4a;
    --night: #0b0b0b;
    --logo-grey: #5c5c5c;
    --list-grey: #8e8e8e;
    --serif: "Cardo", Georgia, serif;
  }
  * { box-sizing: border-box; margin: 0; padding: 0; }
  html, body {
    width: 1200px; height: 926px; overflow: hidden;
    background: var(--backdrop);
    font-family: var(--serif);
  }
  .sheet { position: relative; width: 1200px; height: 926px; }
  .card {
    position: absolute; left: 250px; width: 700px; height: 400px;
    overflow: hidden; box-shadow: 0 6px 18px rgba(0,0,0,.18);
  }
  .card--front { top: 40px; background: var(--paper); }
  .card--back { top: 486px; background: var(--night); }

  .wordmark {
    position: absolute; font-family: var(--serif); font-weight: 400;
    font-size: 26px; line-height: 1.1; letter-spacing: .5px;
  }
  .card--front .wordmark { left: 44px; top: 48px; color: var(--ink); }

  .contact-lines { position: absolute; left: 44px; top: 182px; font-size: 16px; line-height: 1.45; color: var(--ink); }
  .contact-lines .label { color: var(--olive-text); font-weight: 700; }
  .contact-lines em { font-style: italic; }

  .person { position: absolute; right: 44px; top: 200px; text-align: right; }
  .person__name { font-size: 28px; color: var(--olive-text); font-weight: 400; }
  .person__title { font-size: 16px; font-style: italic; color: var(--ink); margin-top: 2px; }
  .person__links { margin-top: 24px; font-size: 17px; line-height: 1.45; color: var(--ink); }

  .swoosh { position: absolute; left: 0; top: 0; width: 700px; height: 400px; }
  .address {
    position: absolute; left: 120px; top: 352px;
    font-size: 17px; letter-spacing: 1px; color: var(--olive-text);
  }

  .card--back .wordmark { left: 0; right: 0; top: 60px; text-align: center; color: var(--logo-grey); font-size: 30px; }
  .product-list {
    position: absolute; left: 30px; right: 30px; top: 128px;
    text-align: center; color: var(--list-grey);
    font-size: 15px; line-height: 1.55; letter-spacing: .8px; text-transform: uppercase;
  }
  .band { position: absolute; left: 0; right: 0; top: 300px; height: 16px; background: var(--olive); }
</style>
</head>
<body>
<main class="sheet">
  <section class="card card--front" aria-label="Card front">
    <div class="wordmark">Copperfield Lantern<br>&amp; Spark, Inc.</div>

    <div class="contact-lines">
      <div><span class="label">cell.</span> 901-555-0147 <em>(office)</em></div>
      <div><span class="label">fax.</span> 901-555-0182</div>
      <div><span class="label">cell.</span> 901-555-0163 <em>(personal)</em></div>
    </div>

    <div class="person">
      <div class="person__name">Marianne T. Holloway</div>
      <div class="person__title">- President/CEO</div>
      <div class="person__links">
        <div>mtholloway@clsllc-example.com</div>
        <div>www.clsincorp-example.com</div>
      </div>
    </div>

    <svg class="swoosh" viewBox="0 0 700 400" aria-hidden="true">
      <path fill="var(--olive)" d="M0 296 C230 298 440 322 700 386 L700 400 C440 350 230 322 0 318 Z"/>
      <path fill="var(--night)" d="M0 318 C230 322 440 350 700 394 L700 400 L0 400 Z"/>
    </svg>
    <div class="address">4728 Quillon Ave., Memphis, TN 38127</div>
  </section>

  <section class="card card--back" aria-label="Card back">
    <div class="wordmark">Copperfield Lantern &amp; Spark, Inc.</div>
    <div class="product-list">
      <div>Boxes &amp; Covers &nbsp; Conduit &amp; Raceway &nbsp; Fittings</div>
      <div>Fuses - Lamp &amp; Ballasts - Lighting Controls &amp; Timers</div>
      <div>Lighting Fixtures - Personal Safety - Pipes - Power Distribution</div>
      <div>Terminations Ground &amp; Splices - Tools &amp; Testers</div>
      <div>Wire, Cords &amp; Cable - Wiring Devices - Valves</div>
    </div>
    <div class="band"></div>
  </section>
</main>
</body>
</html>
```